Custom Home Builder Needs a Website

Harbor Pine Builders Ltd. requires a clean professional 5 page website - Home, About Us, Gallery (Interior and Exterior), Our Process and Contact Us(with registration form). We are a home builder who also has homes for sale. Also please have a place for video embedding. Editable fields by user. Using the stationery 'feel' that is attached. Need social media links. If you require any additional files, please request.

Target Market(s)

Families and professionals

Industry/Entity Type

Home Builder

Coding

Coded - Design and coding required

Number of Pages Required

5+ page

Font styles to use
Sans Serif
Other font styles liked:
• Lato

Requirements
Must have
• Editable by user
• Register Button
• Place to put home models for sale - preferably on the first page
• 5 page website -
• -Home
• -About Us
• -Gallery (Interior and Exterior)
• -Our Process
• -Contact Us.
Nice to have
• Themed similar to current stationery
• place for video embedding
• Try some darker backgrounds
• Change pictures to B/W if works for design
Should not have
• cartoonish type of content

```html
<!DOCTYPE html>
<html lang="en">
<head>
<meta charset="utf-8">
<title>Harbor Pine Builders Ltd.</title>
<link href="https://fonts.googleapis.com/css2?family=Roboto+Condensed:wght@400;700&family=Open+Sans:wght@400;600;700&display=swap" rel="stylesheet">
<style>
:root{
  --green:#5c9e3e;
  --green-dark:#4a8631;
  --ink:#3a3a3a;
  --muted:#6b6b6b;
  --page:#e6e6e6;
  --card:#f1f1f1;
  --search:#6e6e6e;
  --footer:#2b2b2b;
  --footer-base:#1c1c1c;
  --white:#ffffff;
}
*{margin:0;padding:0;box-sizing:border-box}
html,body{width:1200px;height:3383px;overflow:hidden}
body{background:var(--page);font-family:"Open Sans",Arial,sans-serif;color:var(--ink);position:relative}
.heading{font-family:"Roboto Condensed","Arial Narrow",sans-serif;font-weight:700;text-transform:uppercase}
section,header,footer{position:relative;width:1200px}
.abs{position:absolute}

/* hero */
.hero{height:598px;background:linear-gradient(180deg,#9bb4cc 0%,#b9c6cf 35%,#6f7468 70%,#4f5747 100%)}
.hero-photo{position:absolute;inset:0;background:radial-gradient(ellipse at 55% 55%,#6d6e69 0%,#5a5d56 45%,transparent 75%)}
.brand{left:160px;top:14px;width:208px;height:90px;background:var(--white);display:flex;align-items:center;justify-content:center;gap:10px}
.brand-mark{width:14px;height:14px;background:var(--green)}
.brand-name{font-family:"Roboto Condensed",sans-serif;font-weight:700;font-size:17px;color:var(--green);line-height:1.1;text-transform:uppercase}
.topbar{left:368px;top:14px;width:670px;height:51px;background:rgba(255,255,255,.85)}
.contact-item{display:flex;align-items:center;gap:8px;font-size:10px;color:var(--muted);line-height:1.2;white-space:nowrap}
.contact-item b{display:block;font-size:12px;color:var(--ink);font-weight:600}
.icon-dot{width:24px;height:24px;border-radius:50%;background:var(--green);display:flex;align-items:center;justify-content:center;flex:none}
.nav{left:379px;top:65px;height:39px;display:flex;background:var(--white)}
.nav a{display:flex;align-items:center;padding:0 14px;font-size:10px;font-weight:600;color:var(--ink);text-decoration:none;text-transform:uppercase}
.nav a.active{background:var(--green);color:var(--white)}
.nav a.register{background:#4a4a4a;color:var(--white);margin-left:8px}
.navfill{left:873px;top:65px;width:165px;height:39px;background:var(--green)}
.social{left:948px;top:74px;display:flex;gap:6px}
.social span{width:20px;height:20px;border-radius:50%;border:2px solid var(--white)}
.hero-title{left:350px;top:289px;width:500px;height:62px;border-radius:31px;background:rgba(110,110,110,.75);color:var(--white);font-size:31px;display:flex;align-items:center;justify-content:center}
.hero-sub{left:390px;top:356px;width:420px;height:54px;border-radius:27px;background:rgba(110,110,110,.75);color:var(--white);font-size:11px;text-align:center;display:flex;align-items:center;justify-content:center;line-height:1.5}
.btn{display:flex;align-items:center;justify-content:center;gap:10px;border-radius:20px;font-size:11px;font-weight:700;text-transform:uppercase}
.btn-green{left:532px;top:424px;width:138px;height:38px;background:var(--green);color:var(--white)}
.btn-circle{width:16px;height:16px;border-radius:50%;display:flex;align-items:center;justify-content:center}
.side-tab{top:316px;width:28px;height:90px;background:var(--green);color:var(--white);font-size:10px;font-weight:700;letter-spacing:3px;writing-mode:vertical-rl;display:flex;align-items:center;justify-content:center}
.side-tab.prev{left:40px;border-radius:0 14px 14px 0}
.side-tab.next{right:40px;border-radius:14px 0 0 14px}

/* search */
.search{height:209px;background:var(--search)}
.search-title{top:22px;width:100%;text-align:center;color:var(--white);font-size:22px}
.select{width:275px;height:32px;border:1px solid #9a9a9a;border-radius:16px;color:var(--white);font-size:10px;text-transform:uppercase;display:flex;align-items:center;justify-content:space-between;padding:0 16px}
.btn-white{left:532px;top:157px;width:138px;height:39px;background:var(--white);color:var(--ink)}

/* about */
.about{height:388px;background:var(--page)}
.about-photo{left:160px;top:45px;width:429px;height:300px;background:linear-gradient(180deg,#c8d3dc 0%,#b4b7ad 45%,#6e6a5f 75%,#8c8f86 100%)}
.about-frame{left:184px;top:68px;width:381px;height:254px;border:1px solid rgba(255,255,255,.7)}
.about-text{left:611px;top:58px;width:427px}
.eyebrow{color:var(--green);font-size:11px;font-family:"Roboto Condensed",sans-serif}
.about-title{font-size:17px;margin:4px 0 18px;color:var(--ink)}
.about-text p{font-size:10.5px;line-height:1.75;color:var(--muted);margin-bottom:14px}

/* video */
.video{height:449px;background:linear-gradient(135deg,#3a3a3a 0%,#262626 45%,#1c1c1c 100%)}
.play{left:578px;top:204px;width:40px;height:40px}

/* featured */
.featured{height:796px;background:var(--page)}
.section-head{width:100%;text-align:center;color:var(--green);font-size:18px}
.section-icon{left:584px}
.card{width:278px;height:316px;background:var(--card)}
.card-photo{height:185px}
.card-body{padding:14px 12px}
.card-top{display:flex;justify-content:space-between;align-items:baseline}
.card-name{font-family:"Roboto Condensed",sans-serif;font-weight:700;font-size:13px;text-transform:uppercase;color:var(--ink)}
.card-price{font-family:"Roboto Condensed",sans-serif;font-weight:700;font-size:14px;color:var(--green)}
.card-body p{font-size:9.5px;line-height:1.6;color:var(--muted);margin:8px 0 10px}
.card-addr{display:flex;align-items:center;gap:8px;font-size:9.5px;color:var(--ink)}

/* gallery */
.gallery{height:619px;background:var(--page)}
.tile{position:absolute}
.tile-overlay{position:absolute;inset:0;background:rgba(90,90,90,.55);display:flex;align-items:center;justify-content:center}

/* footer */
.footer{height:272px;background:var(--footer);color:#d8d8d8}
.footer-col{top:22px}
.footer-head{color:var(--green);font-size:12px;margin-bottom:26px}
.footer-brand{font-family:"Roboto Condensed",sans-serif;font-weight:700;font-size:15px;color:#bdbdbd;text-transform:uppercase;margin-bottom:24px}
.footer p{font-size:9.5px;line-height:1.7}
.footer-line{display:flex;gap:10px;font-size:9.5px;line-height:1.6;margin-bottom:18px}
.field{width:200px;border:1px solid #777;color:#bbb;font-size:9.5px;padding:6px 8px;margin-top:8px}
.send{width:60px;height:22px;border-radius:11px;background:var(--green);color:var(--white);font-size:9px;font-weight:700;display:flex;align-items:center;justify-content:center;margin-top:10px}
.base{height:52px;background:var(--footer-base);color:#cfcfcf;font-size:10px;display:flex;align-items:center;justify-content:center}
</style>
</head>
<body>

<header class="hero">
  <div class="hero-photo" role="img" aria-label="Exterior photo of a two storey grey craftsman home with stone accents and double garage"></div>

  <div class="abs brand"><span class="brand-mark"></span><span class="brand-name">Harbor Pine<br>Builders</span></div>
  <div class="abs topbar"></div>
  <div class="abs contact-item" style="left:690px;top:22px">
    <span class="icon-dot"><svg width="12" height="12" viewBox="0 0 24 24"><path fill="#fff" d="M6.6 10.8a15 15 0 0 0 6.6 6.6l2.2-2.2c.3-.3.7-.4 1-.2 1.1.4 2.3.6 3.6.6.6 0 1 .4 1 1V20c0 .6-.4 1-1 1A17 17 0 0 1 3 4c0-.6.4-1 1-1h3.5c.6 0 1 .4 1 1 0 1.3.2 2.5.6 3.6.1.3 0 .7-.2 1z"/></svg></span>
    <span>You can call us<b>306-555-0148</b></span>
  </div>
  <div class="abs contact-item" style="left:818px;top:22px">
    <span class="icon-dot"><svg width="12" height="12" viewBox="0 0 24 24"><path fill="#fff" d="M3 5h18v14H3z"/><path fill="none" stroke="#5c9e3e" stroke-width="2" d="M3 6l9 7 9-7"/></svg></span>
    <span>You can mail us<b>info@harborpinebuilders.ca</b></span>
  </div>

  <nav class="abs nav">
    <a class="active">Home</a><a>About Us</a><a>Gallery</a><a>Our Process</a><a>Contact Us</a><a class="register">Register</a>
  </nav>
  <div class="abs navfill"></div>
  <div class="abs social"><span></span><span></span><span></span></div>

  <div class="abs side-tab prev">PREV</div>
  <div class="abs side-tab next">NEXT</div>

  <h1 class="abs hero-title heading">The Best Way to Find Your Home</h1>
  <p class="abs hero-sub">Lorem ipsum consectetur adipiscing elit, sed do eiusmod tempor<br>dolor sit ametconsetetur adipiscing elit, sed do eiusmod tempor incididunt</p>
  <div class="abs btn btn-green">Read More <span class="btn-circle" style="background:#fff"><svg width="8" height="8" viewBox="0 0 8 8"><path d="M2 1l4 3-4 3z" fill="#5c9e3e"/></svg></span></div>
</header>

<section class="search">
  <h2 class="abs search-title heading">Find Your Home Here</h2>
  <div class="abs select" style="left:160px;top:65px">Location<svg width="9" height="6" viewBox="0 0 9 6"><path d="M1 1l3.5 3.5L8 1" stroke="#fff" fill="none" stroke-width="1.4"/></svg></div>
  <div class="abs select" style="left:460px;top:65px">Min Area<svg width="9" height="6" viewBox="0 0 9 6"><path d="M1 1l3.5 3.5L8 1" stroke="#fff" fill="none" stroke-width="1.4"/></svg></div>
  <div class="abs select" style="left:763px;top:65px">Max Area<svg width="9" height="6" viewBox="0 0 9 6"><path d="M1 1l3.5 3.5L8 1" stroke="#fff" fill="none" stroke-width="1.4"/></svg></div>
  <div class="abs select" style="left:160px;top:110px">Number of Badroom<svg width="9" height="6" viewBox="0 0 9 6"><path d="M1 1l3.5 3.5L8 1" stroke="#fff" fill="none" stroke-width="1.4"/></svg></div>
  <div class="abs select" style="left:460px;top:110px">Number of Bathroom<svg width="9" height="6" viewBox="0 0 9 6"><path d="M1 1l3.5 3.5L8 1" stroke="#fff" fill="none" stroke-width="1.4"/></svg></div>
  <div class="abs select" style="left:763px;top:110px">Your Budget<svg width="9" height="6" viewBox="0 0 9 6"><path d="M1 1l3.5 3.5L8 1" stroke="#fff" fill="none" stroke-width="1.4"/></svg></div>
  <div class="abs btn btn-white">Read More <span class="btn-circle" style="background:#3a3a3a"><svg width="8" height="8" viewBox="0 0 8 8"><path d="M2 1l4 3-4 3z" fill="#fff"/></svg></span></div>
</section>

<section class="about">
  <div class="abs about-photo" role="img" aria-label="Photo of a stone and timber family home with front garage"></div>
  <div class="abs about-frame"></div>
  <div class="abs about-text">
    <div class="eyebrow heading">About</div>
    <h2 class="about-title heading">Harbor Pine Builders</h2>
    <p>Lorem Ipsum is simply dummy text of the printing and typesetting industry. Lorem Ipsum has been the industry's standard dummy text ever since the 1500s, when an unknown printer took a galley of type and scrambled it to make a type specimen book.</p>
    <p>It has survived not only five centuries, but also the leap into electronic typesetting, remaining essentially unchanged. It was popularised in the 1960s with the release of transfer sheets containing Lorem Ipsum passages, and more recently with desktop publishing software including many versions of Lorem Ipsum.</p>
    <p>Lorem Ipsum is simply dummy text of the printing and typesetting industry. Lorem Ipsum has been the industry's standard dummy text ever since the 1500s, when an unknown printer took a galley of type and scrambled it to make a type specimen book.</p>
  </div>
</section>

<section class="video" role="img" aria-label="Video still of a dark modern kitchen interior in black and white">
  <svg class="abs play" viewBox="0 0 40 40"><circle cx="20" cy="20" r="18" fill="none" stroke="#fff" stroke-width="2"/><path d="M16 12l11 8-11 8z" fill="#fff"/></svg>
</section>

<section class="featured">
  <svg class="abs section-icon" style="top:48px" width="32" height="20" viewBox="0 0 32 20"><rect x="2" y="8" width="6" height="12" fill="#8a8a8a"/><rect x="10" y="2" width="8" height="18" fill="#6a6a6a"/><rect x="20" y="6" width="6" height="14" fill="#8a8a8a"/><rect x="0" y="19" width="32" height="1" fill="#6a6a6a"/></svg>
  <h2 class="abs section-head heading" style="top:72px">Featured Property</h2>

  <article class="abs card" style="left:160px;top:120px"><div class="card-photo" role="img" aria-label="Photo of a bright kitchen with island and pendant lights" style="background:linear-gradient(135deg,#e7e4de,#a89e8f 60%,#5d4a36)"></div><div class="card-body"><div class="card-top"><span class="card-name">Masons de Villa</span><span class="card-price">$52,350</span></div><p>Dolor sit amet, conse ctetur adipiscing elit, sed do eiusmod tempor incididunt ut labore et lorna aliquatd minim veniam, quis nostrud</p><div class="card-addr"><svg width="9" height="12" viewBox="0 0 9 12"><path d="M4.5 0A4.5 4.5 0 0 0 0 4.5C0 8 4.5 12 4.5 12S9 8 9 4.5A4.5 4.5 0 0 0 4.5 0z" fill="#3a3a3a"/><circle cx="4.5" cy="4.5" r="1.6" fill="#f1f1f1"/></svg>PO Box 218 Eastvale, SK, S0K 2L0</div></div></article>

  <article class="abs card" style="left:460px;top:120px"><div class="card-photo" role="img" aria-label="Photo of a kitchen range with mosaic tile backsplash" style="background:linear-gradient(135deg,#8d8a86,#5f5b57 55%,#3a3633)"></div><div class="card-body"><div class="card-top"><span class="card-name">Masons de Villa</span><span class="card-price">$52,350</span></div><p>Dolor sit amet, conse ctetur adipiscing elit, sed do eiusmod tempor incididunt ut labore et lorna aliquatd minim veniam, quis nostrud</p><div class="card-addr"><svg width="9" height="12" viewBox="0 0 9 12"><path d="M4.5 0A4.5 4.5 0 0 0 0 4.5C0 8 4.5 12 4.5 12S9 8 9 4.5A4.5 4.5 0 0 0 4.5 0z" fill="#3a3a3a"/><circle cx="4.5" cy="4.5" r="1.6" fill="#f1f1f1"/></svg>PO Box 218 Eastvale, SK, S0K 2L0</div></div></article>

  <article class="abs card" style="left:760px;top:120px"><div class="card-photo" role="img" aria-label="Photo of a home office with dark desk and panelled wall" style="background:linear-gradient(180deg,#d9d6cf,#c2bcb1 60%,#6b4e38)"></div><div class="card-body"><div class="card-top"><span class="card-name">Masons de Villa</span><span class="card-price">$52,350</span></div><p>Dolor sit amet, conse ctetur adipiscing elit, sed do eiusmod tempor incididunt ut labore et lorna aliquatd minim veniam, quis nostrud</p><div class="card-addr"><svg width="9" height="12" viewBox="0 0 9 12"><path d="M4.5 0A4.5 4.5 0 0 0 0 4.5C0 8 4.5 12 4.5 12S9 8 9 4.5A4.5 4.5 0 0 0 4.5 0z" fill="#3a3a3a"/><circle cx="4.5" cy="4.5" r="1.6" fill="#f1f1f1"/></svg>PO Box 218 Eastvale, SK, S0K 2L0</div></div></article>

  <article class="abs card" style="left:160px;top:456px"><div class="card-photo" role="img" aria-label="Photo of a child's bedroom with bright quilt" style="background:linear-gradient(180deg,#b9c4c9,#a6b3b6 55%,#c99ab8)"></div><div class="card-body"><div class="card-top"><span class="card-name">Masons de Villa</span><span class="card-price">$52,350</span></div><p>Dolor sit amet, conse ctetur adipiscing elit, sed do eiusmod tempor incididunt ut labore et lorna aliquatd minim veniam, quis nostrud</p><div class="card-addr"><svg width="9" height="12" viewBox="0 0 9 12"><path d="M4.5 0A4.5 4.5 0 0 0 0 4.5C0 8 4.5 12 4.5 12S9 8 9 4.5A4.5 4.5 0 0 0 4.5 0z" fill="#3a3a3a"/><circle cx="4.5" cy="4.5" r="1.6" fill="#f1f1f1"/></svg>PO Box 218 Eastvale, SK, S0K 2L0</div></div></article>

  <article class="abs card" style="left:460px;top:456px"><div class="card-photo" role="img" aria-label="Photo of a dark home exterior with driveway" style="background:linear-gradient(180deg,#7f9ab8,#5e6068 45%,#8a8882)"></div><div class="card-body"><div class="card-top"><span class="card-name">Masons de Villa</span><span class="card-price">$52,350</span></div><p>Dolor sit amet, conse ctetur adipiscing elit, sed do eiusmod tempor incididunt ut labore et lorna aliquatd minim veniam, quis nostrud</p><div class="card-addr"><svg width="9" height="12" viewBox="0 0 9 12"><path d="M4.5 0A4.5 4.5 0 0 0 0 4.5C0 8 4.5 12 4.5 12S9 8 9 4.5A4.5 4.5 0 0 0 4.5 0z" fill="#3a3a3a"/><circle cx="4.5" cy="4.5" r="1.6" fill="#f1f1f1"/></svg>PO Box 218 Eastvale, SK, S0K 2L0</div></div></article>

  <article class="abs card" style="left:760px;top:456px"><div class="card-photo" role="img" aria-label="Photo of a grey stone home with landscaped front yard" style="background:linear-gradient(180deg,#dfe4e8,#6e6f69 50%,#6f8a4e)"></div><div class="card-body"><div class="card-top"><span class="card-name">Masons de Villa</span><span class="card-price">$52,350</span></div><p>Dolor sit amet, conse ctetur adipiscing elit, sed do eiusmod tempor incididunt ut labore et lorna aliquatd minim veniam, quis nostrud</p><div class="card-addr"><svg width="9" height="12" viewBox="0 0 9 12"><path d="M4.5 0A4.5 4.5 0 0 0 0 4.5C0 8 4.5 12 4.5 12S9 8 9 4.5A4.5 4.5 0 0 0 4.5 0z" fill="#3a3a3a"/><circle cx="4.5" cy="4.5" r="1.6" fill="#f1f1f1"/></svg>PO Box 218 Eastvale, SK, S0K 2L0</div></div></article>
</section>

<section class="gallery">
  <svg class="abs section-icon" style="top:19px" width="32" height="20" viewBox="0 0 32 20"><rect x="2" y="8" width="6" height="12" fill="#8a8a8a"/><rect x="10" y="2" width="8" height="18" fill="#6a6a6a"/><rect x="20" y="6" width="6" height="14" fill="#8a8a8a"/><rect x="0" y="19" width="32" height="1" fill="#6a6a6a"/></svg>
  <h2 class="abs section-head heading" style="top:43px">Our Gallery</h2>

  <div class="tile" style="left:160px;top:100px;width:429px;height:230px;background:linear-gradient(180deg,#d6dbdf,#7d7d77 55%,#6e8050)" role="img" aria-label="Gallery photo of a stone and timber home exterior">
    <div class="tile-overlay"><svg width="34" height="34" viewBox="0 0 34 34"><circle cx="17" cy="17" r="15" fill="none" stroke="#fff" stroke-width="1.6"/><path d="M17 11v12M11 17h12" stroke="#fff" stroke-width="1.6"/></svg></div>
  </div>
  <div class="tile" style="left:611px;top:100px;width:203px;height:230px;background:linear-gradient(160deg,#c9b8a4,#8f8478 55%,#4a4440)" role="img" aria-label="Gallery photo of a kitchen counter with glass jars and tile backsplash"></div>
  <div class="tile" style="left:837px;top:100px;width:201px;height:230px;background:linear-gradient(170deg,#f1efea,#d8d0c2 55%,#5a4330)" role="img" aria-label="Gallery photo of a white kitchen with pendant lights"></div>
  <div class="tile" style="left:160px;top:355px;width:203px;height:230px;background:linear-gradient(180deg,#d9d6cf,#c0b9ae 60%,#5d4331)" role="img" aria-label="Gallery photo of a home office with desk and plant"></div>
  <div class="tile" style="left:386px;top:355px;width:203px;height:230px;background:linear-gradient(180deg,#b9c6d0,#dde1e3 50%,#8c8f92)" role="img" aria-label="Gallery photo of a bright bathroom vanity"></div>
  <div class="tile" style="left:611px;top:355px;width:427px;height:230px;background:linear-gradient(180deg,#e0e5e9,#7a7a74 55%,#6a8a4c)" role="img" aria-label="Gallery photo of a grey craftsman home with landscaped lawn"></div>
</section>

<footer class="footer">
  <div class="abs footer-col" style="left:160px;width:270px">
    <h3 class="footer-head heading">About Us</h3>
    <div class="footer-brand">HPB</div>
    <p>Lorem ipsum dolor sit amet, consectetur adipiscing elit. Nunc in dictum enim. Sed eu urna metus. Aenean et est lorem. Vivamus blandit augue at nulla dignissim, quis porttitor nulla iaculis. Ut et porta leo, a ultricies sem. Morbi at elementum diam, sit amet vehicula tellus.</p>
  </div>
  <div class="abs footer-col" style="left:462px;width:250px">
    <h3 class="footer-head heading">Get In Touch</h3>
    <div class="footer-line"><svg width="9" height="12" viewBox="0 0 9 12"><path d="M4.5 0A4.5 4.5 0 0 0 0 4.5C0 8 4.5 12 4.5 12S9 8 9 4.5A4.5 4.5 0 0 0 4.5 0z" fill="#ccc"/><circle cx="4.5" cy="4.5" r="1.6" fill="#2b2b2b"/></svg><span>PO Box 218 Eastvale,<br>SK, S0K 2L0</span></div>
    <div class="footer-line"><svg width="11" height="11" viewBox="0 0 24 24"><path fill="#ccc" d="M6.6 10.8a15 15 0 0 0 6.6 6.6l2.2-2.2c.3-.3.7-.4 1-.2 1.1.4 2.3.6 3.6.6.6 0 1 .4 1 1V20c0 .6-.4 1-1 1A17 17 0 0 1 3 4c0-.6.4-1 1-1h3.5c.6 0 1 .4 1 1 0 1.3.2 2.5.6 3.6.1.3 0 .7-.2 1z"/></svg><span>306-555-0148</span></div>
    <div class="footer-line"><svg width="12" height="10" viewBox="0 0 24 18"><rect width="24" height="18" fill="#ccc"/><path d="M0 1l12 9 12-9" fill="none" stroke="#2b2b2b" stroke-width="2"/></svg><span>info@harborpinebuilders.ca</span></div>
  </div>
  <div class="abs footer-col" style="left:762px;width:276px">
    <h3 class="footer-head heading">Quick Contact</h3>
    <p>Lorem ipsum dolor sit amet, consectetur adipiscing elit.</p>
    <div class="field">Type your email</div>
    <div class="field" style="height:58px">Message</div>
    <div class="send">SEND</div>
  </div>
</footer>
<div class="base">Copyright © 2016 Harbor Pine Builders. All rights reserved.</div>

</body>
</html>
```